Saddle Down at the Stable 2018

I need a flyer that can be printed in both 8.5x 11 and 11x17.
I have uploaded the flyer I used last year just to give you an idea of what I need
This event will include craft beer, live music and food trucks.
The silent auction is an important part of the evening.
It is a fundraiser for Meadow Stride Therapeutic Riding. (we teach horseback riding to special needs children and adults)
I will also need a tshirt design at some point so I would like the logo to be one that is suitable for a tshirt-the tshirt will be a dark color

Target Market(s)

ages 21-55 male and female
horse lovers

Industry/Entity Type

Horseback Riding

Font styles to use
Serif
Sans Serif

Colors

Designer to choose colors to be used in the design.

Requirements
Must have
• horse image
• similar information listed as on the flyer from last year
• second annual 2018
• information about the silent auction
• mention beer, food trucks, live music
• Wagon and Keg logo, lanternfield brewery logo
• November 3, 2018 6:oo-9:00 pm
• $25 ticket price which includes a flight of beer and an event tshirt
• www.mstrinc-example.com to purchase tickets
• Copperleaf Equestrian Center
• 5836 West Marigold Lane
• Woodstock, GA 30188
• barn logo
• email listed for more info: mstrinc@mailbox-example.com
Nice to have
• Please join us for a fundraiser to benefit Meadow Stride Therapeutic Riding, a non-profit organization that provides emotional, physical and social benefits for children and adults with special needs.
Should not have
• Mane Stride

```html
<!DOCTYPE html>
<html lang="en">
<head>
<meta charset="utf-8">
<title>Saddle Down at the Stable</title>
<link rel="stylesheet" href="https://fonts.googleapis.com/css2?family=Allura&family=Oswald:wght@300;400;500;600;700&family=Lato:wght@400;700&display=swap">
<style>
  :root {
    --teal: #1fa58c;
    --teal-script: #3fb8a8;
    --teal-band: #1ba68f;
    --teal-pale: #b9e3dc;
    --white: #ffffff;
    --panel: rgba(243, 241, 236, 0.92);
    --wood-dark: #5a3f28;
    --wood-mid: #8a6644;
    --photo-top: #6e6a64;
    --photo-mid: #4a4038;
  }
  * { margin: 0; padding: 0; box-sizing: border-box; }
  html, body { width: 927px; height: 1200px; overflow: hidden; background: #fff; }
  .flyer {
    position: relative;
    width: 927px;
    height: 1200px;
    overflow: hidden;
    font-family: "Oswald", sans-serif;
    color: var(--white);
  }
  .backdrop {
    position: absolute; inset: 0 0 146px 0;
    background: linear-gradient(180deg, var(--photo-top) 0%, #5c5852 22%, var(--photo-mid) 40%, var(--wood-mid) 52%, #7a5a3c 75%, var(--wood-dark) 100%);
  }
  .venue-mark {
    position: absolute; left: 730px; top: 50px; width: 154px; height: 154px;
    display: flex; align-items: center; justify-content: center; text-align: center;
  }
  .venue-mark svg { position: absolute; inset: 0; }
  .venue-mark span {
    position: relative; font-weight: 500;
    font-size: 15px; line-height: 19px; letter-spacing: 1px; text-transform: uppercase; color: var(--white);
  }
  .edition {
    position: absolute; left: 44px; top: 300px;
    font-weight: 400; font-size: 20px; line-height: 24px; letter-spacing: 4px;
  }
  .title-script {
    position: absolute; left: 30px; top: 322px;
    font-family: "Allura", cursive; font-size: 118px; line-height: 1;
    color: var(--teal-script); white-space: nowrap;
  }
  .title-small {
    position: absolute; left: 50px; top: 470px; width: 100px;
    border-top: 3px solid var(--white); border-bottom: 3px solid var(--white);
    padding: 8px 0; text-align: center;
    font-weight: 300; font-size: 28px; line-height: 36px; letter-spacing: 1px;
  }
  .title-block {
    position: absolute; left: 160px; top: 444px;
    font-weight: 700; font-size: 104px; line-height: 1; letter-spacing: -2px;
    white-space: nowrap;
  }
  .intro {
    position: absolute; left: 42px; top: 594px; width: 412px;
    font-weight: 300; font-size: 27px; line-height: 34.5px; letter-spacing: -0.4px;
  }
  .intro strong { font-weight: 600; }
  .price {
    position: absolute; left: 37px; top: 832px; width: 340px;
    font-weight: 300; font-size: 27px; line-height: 33px; letter-spacing: -0.4px;
  }
  .price strong { font-weight: 700; }
  .auction-heading {
    position: absolute; left: 37px; top: 922px;
    font-weight: 700; font-size: 30px; line-height: 36px; letter-spacing: -0.8px;
  }
  .auction-items {
    position: absolute; left: 37px; top: 958px; width: 380px;
    display: grid; grid-template-columns: 207px 1fr;
    font-weight: 300; font-size: 27px; line-height: 32px; letter-spacing: -0.4px;
  }
  .highlights {
    position: absolute; left: 490px; top: 492px; list-style: none;
  }
  .highlights li {
    display: flex; align-items: center; height: 50px;
    font-weight: 400; font-size: 34px; letter-spacing: -0.5px; white-space: nowrap;
  }
  .highlights svg { width: 48px; height: 42px; margin-right: 10px; }
  .details {
    position: absolute; left: 452px; top: 702px; width: 448px; height: 320px;
    background: var(--panel); color: var(--teal); text-align: center;
  }
  .details .date {
    margin-top: 16px; font-weight: 700; font-size: 56px; line-height: 64px; letter-spacing: -2px;
  }
  .details .time {
    margin-top: 12px; display: flex; align-items: center; justify-content: center; gap: 10px;
    font-weight: 500; font-size: 52px; line-height: 60px; letter-spacing: -1px;
  }
  .details .time::before, .details .time::after {
    content: ""; width: 30px; height: 5px; background: var(--teal);
  }
  .details .venue {
    margin-top: 20px; font-weight: 400; font-size: 30px; line-height: 40px; letter-spacing: -0.8px;
  }
  .details .address {
    margin-top: 6px; font-weight: 300; font-size: 26px; line-height: 44px; letter-spacing: -0.5px;
  }
  .band-edge {
    position: absolute; left: 0; top: 1042px; width: 927px; height: 12px; background: var(--teal-pale);
  }
  .footer {
    position: absolute; left: 0; top: 1054px; width: 927px; height: 146px; background: var(--teal-band);
  }
  .contact {
    position: absolute; left: 39px; top: 18px;
    font-family: "Lato", sans-serif; font-size: 18px; line-height: 27px;
  }
  .contact strong { font-family: "Oswald", sans-serif; font-weight: 500; font-size: 20px; }
  .contact .tickets { margin-top: 16px; }
  .contact .tickets strong { font-size: 24px; font-weight: 600; }
  .sponsor {
    position: absolute; font-weight: 600;
    color: var(--white); text-align: center; text-transform: uppercase;
  }
  .sponsor-wagon { left: 458px; top: 52px; width: 196px; font-size: 28px; line-height: 34px; }
  .sponsor-lantern { left: 688px; top: 20px; width: 210px; display: flex; flex-direction: column; align-items: center; }
  .sponsor-lantern svg { width: 40px; height: 40px; margin-bottom: 6px; }
  .sponsor-lantern span { font-size: 24px; line-height: 30px; }
</style>
</head>
<body>
<main class="flyer">
  <div class="backdrop" role="img" aria-label="Photo of a woman greeting a dark horse in a barn doorway, fading into a weathered wooden plank background"></div>

  <div class="venue-mark">
    <svg viewBox="0 0 154 154" aria-hidden="true"><circle cx="77" cy="77" r="73" fill="none" stroke="#fff" stroke-width="3"/></svg>
    <span>Copperleaf<br>Equestrian<br>Center</span>
  </div>

  <p class="edition">SECOND ANNUAL · 2018</p>

  <h1>
    <span class="title-script">Saddle Down</span>
    <span class="title-small">AT THE</span>
    <span class="title-block">STABLE</span>
  </h1>

  <p class="intro">Please join us for a fundraiser to benefit <strong>Meadow Stride Therapeutic Riding Center</strong>, a non-profit organization that provides emotional, physical and social benefits for children and adults with special needs.</p>

  <p class="price"><strong>$25</strong> which includes a flight of beer and an event t-shirt</p>

  <h2 class="auction-heading">SILENT AUCTION ITEMS INCLUDE:</h2>
  <div class="auction-items">
    <span>Ember Dome Grill</span><span>Home Decor</span>
    <span>Vacation Rentals</span><span>Jewelry &amp; More</span>
  </div>

  <ul class="highlights">
    <li><svg viewBox="0 0 48 42" aria-hidden="true"><path d="M4 24 L16 36 L44 4" fill="none" stroke="#fff" stroke-width="5"/></svg>CRAFT BEER</li>
    <li><svg viewBox="0 0 48 42" aria-hidden="true"><path d="M4 24 L16 36 L44 4" fill="none" stroke="#fff" stroke-width="5"/></svg>FOOD TRUCKS</li>
    <li><svg viewBox="0 0 48 42" aria-hidden="true"><path d="M4 24 L16 36 L44 4" fill="none" stroke="#fff" stroke-width="5"/></svg>LIVE MUSIC</li>
    <li><svg viewBox="0 0 48 42" aria-hidden="true"><path d="M4 24 L16 36 L44 4" fill="none" stroke="#fff" stroke-width="5"/></svg>SILENT AUCTION &amp; RAFFLES</li>
  </ul>

  <section class="details">
    <p class="date">NOVEMBER 3, 2018</p>
    <p class="time">6:00PM - 9:00PM</p>
    <p class="venue">COPPERLEAF EQUESTRIAN CENTER</p>
    <p class="address">5836 WEST MARIGOLD LANE<br>WOODSTOCK, GA 30188</p>
  </section>

  <div class="band-edge"></div>
  <footer class="footer">
    <div class="contact">
      <p>For More information,</p>
      <p>Please contact: <strong>mstrinc@mailbox-example.com</strong></p>
      <p class="tickets">Purchase Tickets at <strong>www.mstrinc-example.com</strong></p>
    </div>
    <div class="sponsor sponsor-wagon">Wagon and Keg</div>
    <div class="sponsor sponsor-lantern">
      <svg viewBox="0 0 40 40" aria-hidden="true"><circle cx="20" cy="20" r="18" fill="#fff"/></svg>
      <span>Lanternfield<br>Brewery</span>
    </div>
  </footer>
</main>
</body>
</html>
```